Hot-air ballooning company needs a DL-size flyer

Skylark Aerial Tours is a hot-air ballooning company which flies passengers in the King Valley, Victoria, Australia.
We need a 2-sided DL-size flyer which promotes our hot-air balloon flights and packages.
Most of our customers are couples, and we want the flyer design to communicate safety, adventure, and romance.
The flyer should make the best use of our images which we provide, and we've also included a document with the text for the flyer.
Updates

2 days is not long enough to gather designs, the brief never asked me what my deadline should be.

Target Market(s)

Couples, buyers are majority female, between the ages of 20-60

Industry/Entity Type

Tourism

Font styles to use
Sans Serif

Colors

Designer to choose colors to be used in the design.

Requirements
Must have
• Communicate safety, adventure, and romance
• Use images
Nice to have
• There is a lot of text, it would be great if you could make it look like as little text as possible
Should not have
• No childish designs

```html
<!DOCTYPE html>
<html lang="en">
<head>
<meta charset="utf-8">
<title>Skylark Aerial Tours – Flyer</title>
<link href="https://fonts.googleapis.com/css2?family=Arimo:wght@400;700&display=swap" rel="stylesheet">
<style>
  :root {
    --ink: #1d2226;
    --ink-deep: #1f2f45;
    --paper: #ffffff;
    --gold: #f5b31c;
    --gold-light: #fbd27a;
    --shadow: #b9b9b9;
  }
  * { box-sizing: border-box; margin: 0; padding: 0; }
  html, body { width: 1200px; height: 2520px; overflow: hidden; background: var(--paper); }
  body { font-family: "Arimo", Arial, sans-serif; color: var(--ink); }
  .flyer { position: relative; width: 1200px; height: 2520px; background: var(--paper); overflow: hidden; }

  .intro { position: absolute; left: 122px; top: 340px; width: 960px; font-size: 37px; line-height: 1.32; }
  .intro .lead { font-weight: 700; font-size: 42px; }
  .intro p { margin-bottom: 34px; }

  .flight { position: absolute; left: 122px; top: 1040px; width: 960px; }
  .flight h2 { font-size: 56px; font-weight: 400; margin-bottom: 36px; }
  .flight ul { list-style: none; font-size: 36px; line-height: 1.3; }
  .flight li { position: relative; padding-left: 28px; margin-bottom: 6px; }
  .flight li::before { content: "•"; position: absolute; left: 0; }

  .gold-band { position: absolute; left: 0; top: 1780px; width: 1200px; height: 740px; background: var(--gold); }

  .facts {
    position: absolute; left: 226px; top: 1700px; width: 826px; height: 410px;
    background: var(--paper);
    box-shadow: 0 -18px 0 0 var(--shadow), -14px 0 0 0 #d6d6d6, 14px 0 0 0 #d6d6d6;
    padding: 56px 0 0 100px;
  }
  .facts ul { list-style: none; font-size: 33px; line-height: 1.3; }
  .facts li { position: relative; padding-left: 30px; }
  .facts li::before { content: "•"; position: absolute; left: 0; }

  .bookings { position: absolute; left: 0; top: 2160px; width: 1200px; text-align: center; color: var(--ink-deep); font-size: 35px; line-height: 1.35; }
  .bookings strong { font-weight: 700; }

  .social { position: absolute; left: 0; top: 2300px; width: 1200px; height: 124px; background: var(--gold-light); text-align: center; padding-top: 14px; font-size: 35px; line-height: 1.35; color: var(--ink-deep); }

  .certificate { position: absolute; left: 0; top: 2438px; width: 1200px; text-align: center; font-size: 33px; line-height: 1.35; color: var(--ink-deep); }
</style>
</head>
<body>
<main class="flyer">
  <section class="intro">
    <p><span class="lead">Live the romance and adventure of flying the beautiful King Valley and surrounds</span> in a hot-air balloon at dawn. From the vineyards and patchwork of fields the views expand to the Ovens River, spectacular Mt Buffalo and the High Country beyond. The mountain views, once aloft, come to life in dramatic 3D with the early morning light.</p>
    <p>Celebrate your flight with a delicious breakfast afterwards (optional)</p>
    <p>Milawa is conveniently located less than an hour's drive from most places in Victoria's North East and Albury in NSW. Mansfield flights are also available.</p>
  </section>

  <section class="flight">
    <h2>Your flight</h2>
    <ul>
      <li>One-hour sunrise balloon flight in the spectacular King Valley region in North East Victoria</li>
      <li>Delicious champagne breakfast after the flight (recommended option)</li>
      <li>Informative details throughout your experience with our locally based expert crew</li>
      <li>The opportunity to be involved in the inflation and deflation process should you wish</li>
    </ul>
  </section>

  <div class="gold-band"></div>

  <section class="facts">
    <ul>
      <li>Safe, friendly and professional</li>
      <li>The flight lasts approximately 1 hour</li>
      <li>The entire experience takes about 3-4 hours</li>
      <li>Suitable from age 7 to 97</li>
      <li>Gift Vouchers are also available</li>
      <li>Contact us for exclusive flight options at your custom location</li>
    </ul>
  </section>

  <section class="bookings">
    <p>For bookings or more information:</p>
    <p><strong>www.skylarkaerialtours.com.au | flights@skylarkaerialtours.com.au</strong></p>
    <p>or call our friendly team on <strong>1300 759 527</strong></p>
  </section>

  <section class="social">
    <p>Find us also on Friendbook, Snapgram and TravelRate</p>
    <p>@skylarkaerialtours</p>
  </section>

  <section class="certificate">
    <p>Skylark Aerial Tours operates under Air Operator's Certificate AOC-4471-09</p>
    <p>issued by the National Air Safety Regulator</p>
  </section>
</main>
</body>
</html>
```